Flyer-Design für meine Tätigkeit als freier Trauerredner
Zielgruppe
Für meine Tatigkeit als freier Trauerredner bei Beerdigungen möchte ich einen Flyer designen lassen, um diesen bei Bestattern aufzulegen sowie diese grundsätzlich als Informationsmaterial an interessierte Personen weitergeben zu können. Zielgruppe sind einerseits Personen, die sich lange im Vorfeld Gedanken über den Tod machen und den Wunsch äußern, im Rahmen einer persönlichen Gedenkfeier, unabhängig einer Konfessionszugehörigkeit und der Kirche verabschiedet zu werden. Auf der anderen Seite ist der Flyer ebenso für trauendernde Angehörige gedacht, die aufgrund eines unerwarteten Todesfalls sich mit dem Thema Beerdigung auseinadersetzen müssen und nach Alternativen zu einer krichlichen Beerdiugung suchen.
Aufgabenstellung
Eine Visitenkarte scheint mir im Format zu klein ... ein Flyer in einem größeren Format scheint mir geeigneter, Informationen zu vermitteln. Eine große Stärke von mir ist meine Emapthie. Der Flyer soll dies in der Bildsprache ausdrücken. Ebenso soll der Flyer durch die Bilder und die gewählte Sprahce Vertrauen aufbauen. Tod und Beerdigung sind für viele ein Tabuthemen ... der Flyer soll hier eine Brücke schlagen.
Wichtig wäre mir den Ablauf der Vorbereitung im Flyer aufzuskizzieren, um zu wissen, wie die Vorbereitung und Druchführung beispielhaft erfolgt.
Meine Kernaussage:
Freie Trauerreden, so einzigartig und besonders wie jeder Mensch selbst!
Als freier Trauerredner ist es mein Anspruch, den schweren Moment des Abschiednehmens so persönlich und würdevoll wie nur möglich zu gestalten!
Mein Ziel: Herzensverbindungen zwischen Menschen aufleben zu lassen und diese zu stärken. Herzensverbindungen leben und wirken weiter – unabhängig ob im Leben oder über den Tod hinaus!
Alle Informationen, die im Flyer aufgeführt werden sollen, sind dem beigefügten Word-Dokument zu entnehmen.
Wichtige Information finden Sie auf meiner Website www.tobiaskrämer.com
Wenn ein Statement oder Reszession benötigt wird und sich gut im Flyer macht, liefere ich diese gerne nach.

```html
<!DOCTYPE html>
<html lang="de">
<head>
<meta charset="utf-8">
<title>Flyer Tobias Krämer – DIN A5 Klapp 4-seitig</title>
<link href="https://fonts.googleapis.com/css2?family=Cormorant+Garamond:ital,wght@0,400;0,500;0,600;1,500&family=Montserrat:ital,wght@0,400;0,600;0,700;1,400&display=swap" rel="stylesheet">
<style>
  :root{
    --canvas:#e3e3e3;
    --paper:#ffffff;
    --brown:#8a4f2b;
    --ink:#4a3a30;
    --ink-soft:#6b5a4e;
    --title:#4a2b1a;
    --serif:"Cormorant Garamond", Georgia, serif;
    --sans:"Montserrat", Arial, sans-serif;
  }
  *{box-sizing:border-box;margin:0;padding:0}
  html,body{width:1200px;height:2514px;overflow:hidden;background:var(--canvas)}
  body{position:relative;font-family:var(--sans);color:var(--ink)}

  .sheet-title{position:absolute;left:58px;top:52px;font-family:var(--serif);color:var(--title)}
  .sheet-title h1{font-size:36px;font-weight:600;line-height:1}
  .sheet-title p{font-family:var(--sans);font-size:20px;margin:8px 0 0 52px;color:var(--title)}

  .page{position:absolute;width:520px;height:737px;background:var(--paper);overflow:hidden;box-shadow:0 6px 18px rgba(0,0,0,.12)}
  .spread-fold{position:absolute;width:1px;height:737px;background:rgba(0,0,0,.08)}

  /* cover */
  .cover-photo{position:absolute;left:0;top:0;width:520px;height:470px;
    background:radial-gradient(circle at 70% 18%,#fff3cf 0%,#f6b859 16%,#d98c3a 38%,#8c5a36 65%,#4b3324 100%)}
  .frame-light{position:absolute;left:26px;right:26px;top:26px;height:444px;border:1px solid rgba(255,255,255,.9);border-bottom:none}
  .frame-dark{position:absolute;left:26px;right:26px;top:470px;bottom:26px;border:1px solid var(--brown);border-top:none}
  .cover-name{position:absolute;left:0;right:0;top:372px;text-align:center;color:#fff;font-family:var(--serif)}
  .cover-name .name{font-size:40px;letter-spacing:5px;font-weight:500;line-height:1}
  .cover-name .role{font-size:19px;letter-spacing:2.5px;margin-top:4px}
  .cover-text{position:absolute;left:40px;right:40px;top:484px;text-align:center}
  .cover-text h2{font-family:var(--serif);font-style:italic;font-weight:500;font-size:22px;line-height:1.15;color:var(--ink)}
  .cover-text .lead{font-size:10.5px;line-height:1.45;margin-top:12px;color:var(--ink-soft);font-style:italic}
  .cover-text .cta{font-family:var(--serif);font-size:16px;margin-top:14px;color:var(--ink)}
  .cover-contacts{position:absolute;left:40px;right:40px;top:670px;display:flex;justify-content:space-between;font-size:10px;color:var(--brown)}
  .cover-contacts div{text-align:center;width:150px}
  .icon{width:14px;height:14px;display:block;margin:0 auto 3px;stroke:var(--brown);fill:none;stroke-width:1.3}

  /* inner pages */
  .page-photo{position:absolute;inset:0}
  .inner-left .page-photo{background:linear-gradient(160deg,#d9cfc6 0%,#efe8e1 35%,#e6ddd3 60%,#cbbdb0 100%)}
  .inner-right .page-photo{background:linear-gradient(200deg,#ece6e0 0%,#f7f3ef 40%,#eee6dd 70%,#ddd0c3 100%)}
  .veil{position:absolute;inset:0;background:rgba(255,255,255,.55)}
  .frame{position:absolute;left:26px;right:26px;top:26px;bottom:26px;border:1px solid var(--brown)}
  .page-heading{position:absolute;left:0;right:0;top:50px;text-align:center;font-family:var(--serif);font-size:19px;letter-spacing:5px;color:var(--ink);font-weight:500}
  .body-copy{position:absolute;left:48px;right:48px;top:92px;font-size:9.6px;line-height:1.42;color:var(--ink)}
  .body-copy h3{font-size:9.8px;font-weight:700;margin-top:9px}
  .body-copy h3:first-child{margin-top:0}
  .body-copy ul{margin:2px 0 0 14px}
  .body-copy li{margin-bottom:1px}
  .body-copy a{color:var(--brown);text-decoration:underline}
  .body-copy em{color:var(--ink-soft)}

  /* back page */
  .back .page-photo{background:linear-gradient(180deg,#f1f1f1 0%,#dfe6ee 35%,#cdd6df 55%,#f3ede6 100%)}
  .portrait{position:absolute;left:0;bottom:0;width:300px;height:410px;
    background:radial-gradient(ellipse at 45% 30%,#d8b59a 0%,#b98e6e 25%,#6a5446 55%,#3c312c 100%);opacity:.9}
  .about{position:absolute;left:200px;right:48px;top:110px;font-size:11.5px;line-height:1.55;color:var(--ink)}
  .about h3{font-size:11.5px;font-weight:700;font-style:italic;margin-bottom:6px}
  .contact{position:absolute;left:300px;right:40px;top:500px;font-size:11px;line-height:1.4;color:var(--ink)}
  .contact h3{font-size:11px;font-weight:700;margin-bottom:6px}
  .contact .row{display:flex;align-items:flex-start;gap:8px;margin-top:6px}
  .contact .icon{margin:1px 0 0}
</style>
</head>
<body>

<header class="sheet-title">
  <h1>Flyer TOBIAS KRÄMER</h1>
  <p>DIN A5 Klapp 4-seitig</p>
</header>

<!-- Titelseite -->
<section class="page cover" style="left:340px;top:140px">
  <div class="cover-photo" role="img" aria-label="Foto: Trauerredner im warmen Gegenlicht"></div>
  <div class="frame-light"></div>
  <div class="frame-dark"></div>
  <div class="cover-name"><div class="name">TOBIAS KRÄMER</div><div class="role">Freier Trauerredner</div></div>
  <div class="cover-text">
    <h2>Freie Gedenkfeiern,<br>so einzigartig und besonders wie jeder Mensch selbst!</h2>
    <p class="lead">Mein Ziel ist es, Herzensverbindungen zwischen Menschen aufleben zu lassen und zu stärken. Herzensverbindungen leben und wirken weiter – unabhängig ob im Leben oder über den Tod hinaus!</p>
    <p class="cta">Kostenfreies Informationsgespräch mit Tobias Krämer vereinbaren</p>
  </div>
  <div class="cover-contacts">
    <div><svg class="icon" viewBox="0 0 16 16"><path d="M4 1.5l2.5 3-1.5 1.5c.8 2 2.5 3.7 4.5 4.5L11 9l3 2.5-1.5 2.5C7 14 2 9 2 3z"/></svg>+49 170 5550142</div>
    <div><svg class="icon" viewBox="0 0 16 16"><rect x="1.5" y="3.5" width="13" height="9"/><path d="M1.5 3.5L8 9l6.5-5.5"/></svg>info@tobiaskrämer.com</div>
    <div><svg class="icon" viewBox="0 0 16 16"><rect x="1.5" y="2.5" width="13" height="9"/><path d="M5.5 14h5M8 11.5V14"/></svg>www.tobiaskrämer.com</div>
  </div>
</section>

<!-- Innenseiten -->
<section class="page inner-left" style="left:80px;top:940px">
  <div class="page-photo" role="img" aria-label="Zartes, verblasstes Stimmungsfoto als Seitenhintergrund"></div>
  <div class="veil"></div>
  <div class="frame"></div>
  <h2 class="page-heading">ALLGEMEINE INFORMATIONEN</h2>
  <div class="body-copy">
    <h3>Was ist eine freie Trauerfeier/Gedenkfeier?</h3>
    <p>Freie Trauerzeremonie, Gedenkfeier, Beerdigung, Lebensabschiedsfeier … Synonyme für eine von mir als <b>freier Trauerredner</b> durchgeführte <b>Abschiedszeremonie, die ganz individuell und persönlich auf die verstorbene Person oder das verstorbene Kind bezogen ist</b> – weltlich frei, unabhängig einer Konfession mit individuellem Ablauf.</p>
    <h3>Orte für freie Trauerfeiern</h3>
    <p>Freie Trauerfeiern finden meist auf Friedhöfen, in Kapellen oder Aussegnungshallen, auf dem Friedhofsgelände, einem Waldfriedhof oder auch in den Räumen des Bestatters statt. Auch ein selbstgewählter Ort in der Natur kann unter Voraussetzungen möglich sein.</p>
    <h3>Eine freie Trauerzeremonie beinhaltet im Wesentlichen folgende Elemente:</h3>
    <ul>
      <li>Gedenken an die verstorbene Person in einem feierlichen Rahmen</li>
      <li>Herausstellen der einzigartigen Persönlichkeit und des Charakters der Person – würdevoll in den Mittelpunkt gestellt</li>
      <li>Aufleben lassen wertvoller Erinnerungen und Ausdruck der Dankbarkeit an die gemeinsamen Stunden</li>
      <li>der Trauer Raum zu geben und damit Stärkung der Herzensverbindung</li>
      <li>Beistand, Trost und Zuspruch erfahren – durch die anwesenden Trauergäste, den freien Trauerredner, alles Verbindende und/oder das Größere</li>
    </ul>
    <h3>Dauer einer freien Trauerfeier</h3>
    <p>Eine freie Trauerfeier dauert in der Regel <b>20 - 30 Minuten</b>.</p>
    <h3>Kosten der Trauerrede / Gedenkfeier</h3>
    <p>Die Kosten für die Trauerrede bzw. der Umrahmung der Gedenkfeier betragen <b>419 EUR</b> inkl. MwSt. Die Pauschale beinhaltet das Vorbereitungsgespräch sowie die Aufbereitung und Durchführung der freien Trauerrede, die Sie zum Nachlesen als persönliches Exemplar erhalten. Die Fahrtkosten betragen 55 Cent je Kilometer für die Fahrt zum Friedhof bzw. Ort der Verabschiedung und zurück.</p>
  </div>
</section>
<div class="spread-fold" style="left:600px;top:940px"></div>
<section class="page inner-right" style="left:600px;top:940px">
  <div class="page-photo" role="img" aria-label="Zartes, verblasstes Stimmungsfoto mit Gräsern als Seitenhintergrund"></div>
  <div class="veil"></div>
  <div class="frame"></div>
  <h2 class="page-heading">VORBEREITUNG/ABLAUF</h2>
  <div class="body-copy">
    <h3>Lichtvolle - würdevolle - persönliche Wege des Abschieds - Vorbereitung und Ablauf</h3>
    <p>Detailinformationen zu den einzelnen Punkten finden Sie im Internet unter <a>www.tobiaskrämer.com</a></p>
    <h3>Überlegung im Vorfeld:</h3>
    <p>Es ist gut, im ersten Schritt der Planung einer freien Trauerfeier grundsätzlichen Überlegungen Raum zu geben, wie zum Beispiel:</p>
    <ul>
      <li><em>Hat die/der Verstorbene im Vorfeld Wünsche zur eigenen Beerdigung geäußert?</em></li>
      <li><em>Wie sollte die freie Trauerfeier ablaufen, damit die Gedenkfeier „stimmig“ ist – für die verstorbene Person, Sie selbst, Familie, Freunde und sie diese später in guter Erinnerung behalten?</em></li>
    </ul>
    <h3>Das Vorbereitungsgespräch - Dauer ca. 2 Stunden</h3>
    <p>Persönlich, telefonisch oder digital werden in einem Vorbereitungsgespräch alle wichtigen Informationen zur verstorbenen Person gesammelt und gemeinsam der Ablauf der freien Gedenkfeier geplant.</p>
    <h3>Ablauf der Gedenkfeier - Dauer ca. 20 - 30 Minuten</h3>
    <p>Den Möglichkeiten des Ablaufs einer freien Trauerfeier sind wenig Grenzen gesetzt - Ihre Bedürfnisse und Wünsche stehen im Mittelpunkt! Es betragen 55 Cent je Kilometer für die Fahrt zum Friedhof bzw. Ort der Verabschiedung und zurück.</p>
    <h3>Wichtige Elemente:</h3>
    <ul>
      <li><b>Persönliche Worte</b> in Form einer individuellen Trauerrede zur Würdigung des Lebens der verstorbenen Person</li>
      <li><b>Ausgewählte Musikstücke</b></li>
      <li><b>Aktive Beteiligung Ihrerseits, von Angehörigen und/oder Freunden</b> durch das Vorlesen eines Gedichts, eines Gebets oder persönlich verfasster Worte</li>
      <li><b>Rituale des Gedenkens</b> können einen würdevollen, persönlichen Beitrag umrahmen und in verschiedenster Weise integriert werden, z.B. Seifenblasen, Briefe/Wünsche, eine Lichterkranz der Verbundenheit oder Wunderkerzen zum Schluss einer Gedenkfeier, um symbolisch Sterne der Liebe und Dankbarkeit regnen zu lassen…</li>
    </ul>
  </div>
</section>

<!-- Außenseiten -->
<section class="page back" style="left:80px;top:1740px">
  <div class="page-photo" role="img" aria-label="Heller, unscharfer Hintergrund am Wasser"></div>
  <div class="portrait" role="img" aria-label="Porträtfoto des Trauerredners im Sonnenlicht"></div>
  <div class="frame"></div>
  <h2 class="page-heading">ZU MEINER PERSON</h2>
  <div class="about">
    <h3>Freier Trauerredner Tobias Krämer</h3>
    <p>Freier Trauerredner zu sein ist meine Berufung! Mir ist es eine Freude, Menschen Halt und Kraft zu geben! Das ist mein Anspruch – sowohl als freier Trauerredner im Moment des Abschiednehmens, aber auch als Coach, wenn es darum geht, wieder Halt und Kraft im Leben zu finden!</p>
  </div>
  <div class="contact">
    <h3>Kontakt</h3>
    <p>Tobias Krämer</p>
    <div class="row"><svg class="icon" viewBox="0 0 16 16"><path d="M8 15s5-5.5 5-9a5 5 0 0 0-10 0c0 3.5 5 9 5 9z"/><circle cx="8" cy="6" r="1.8"/></svg><span>Lindenweg 8<br>84030 Musterstadt</span></div>
    <div class="row"><svg class="icon" viewBox="0 0 16 16"><path d="M4 1.5l2.5 3-1.5 1.5c.8 2 2.5 3.7 4.5 4.5L11 9l3 2.5-1.5 2.5C7 14 2 9 2 3z"/></svg><span>0170 5550142</span></div>
    <div class="row"><svg class="icon" viewBox="0 0 16 16"><rect x="1.5" y="3.5" width="13" height="9"/><path d="M1.5 3.5L8 9l6.5-5.5"/></svg><span>info@tobiaskrämer.com</span></div>
    <div class="row"><svg class="icon" viewBox="0 0 16 16"><rect x="1.5" y="2.5" width="13" height="9"/><path d="M5.5 14h5M8 11.5V14"/></svg><span>www.tobiaskrämer.com</span></div>
  </div>
</section>
<section class="page cover" style="left:600px;top:1740px">
  <div class="cover-photo" role="img" aria-label="Foto: Trauerredner im warmen Gegenlicht"></div>
  <div class="frame-light"></div>
  <div class="frame-dark"></div>
  <div class="cover-name"><div class="name">TOBIAS KRÄMER</div><div class="role">Freier Trauerredner</div></div>
  <div class="cover-text">
    <h2>Freie Gedenkfeiern,<br>so einzigartig und besonders wie jeder Mensch selbst!</h2>
    <p class="lead">Mein Ziel ist es, Herzensverbindungen zwischen Menschen aufleben zu lassen und zu stärken. Herzensverbindungen leben und wirken weiter – unabhängig ob im Leben oder über den Tod hinaus!</p>
    <p class="cta">Kostenfreies Informationsgespräch mit Tobias Krämer vereinbaren</p>
  </div>
  <div class="cover-contacts">
    <div><svg class="icon" viewBox="0 0 16 16"><path d="M4 1.5l2.5 3-1.5 1.5c.8 2 2.5 3.7 4.5 4.5L11 9l3 2.5-1.5 2.5C7 14 2 9 2 3z"/></svg>+49 170 5550142</div>
    <div><svg class="icon" viewBox="0 0 16 16"><rect x="1.5" y="3.5" width="13" height="9"/><path d="M1.5 3.5L8 9l6.5-5.5"/></svg>info@tobiaskrämer.com</div>
    <div><svg class="icon" viewBox="0 0 16 16"><rect x="1.5" y="2.5" width="13" height="9"/><path d="M5.5 14h5M8 11.5V14"/></svg>www.tobiaskrämer.com</div>
  </div>
</section>
<div class="spread-fold" style="left:600px;top:1740px"></div>

</body>
</html>
```